Stationary Set Rebrand for Brenvik

We are a Canadian Distribution and Service Company that was established in 1969. Over the past 5 decades we have expanded our business and have warehouses across Canada. We specialize in adhesive tapes, adhesives, films, safety, warehouse, shipping, janitorial and packaging supplies.

We have updated our logo design and would like a new corporate branding identity that includes a new fresh Stationary Set (Business Cards, Letterhead, Letterhead MS Word, Envelope, Presentation Folders, Email Signatures, Notepad Covers, etc.)

Target Market(s)

Industrial Business Sector

Font styles to use
Sans Serif

Colors
0054AA
0677BA
7BADD7
CADEEF
E8F1F8
0094D4
00A9DD
6FCCEA
C7EBF8
E9F6FB
00AB8E
00BBA5
67D7C9
C6EFE9
E9F9F6
EB3D1F
EC4F4E
F09395
F8D3D4
FCEDEE

Requirements
Should not have
• Colors not too light, darker colours preferred

```html
<!DOCTYPE html>
<html lang="en">
<head>
<meta charset="utf-8">
<title>Brenvik Stationery Set</title>
<link href="https://fonts.googleapis.com/css2?family=Poppins:wght@400;500;700;800&family=Open+Sans:wght@400;600;700&display=swap" rel="stylesheet">
<style>
:root{
  --ink:#1c1b27;
  --ink-soft:#2a2935;
  --red:#e31b2c;
  --red-deep:#b5141f;
  --paper:#ffffff;
  --stage:#d9dfe3;
  --text:#1f1f1f;
  --muted:#3a3a3a;
  --line:#cfd3d6;
  --tint:#f7e6e0;
}
*{box-sizing:border-box;margin:0;padding:0}
html,body{width:1200px;height:711px;overflow:hidden}
body{background:var(--stage);font-family:"Open Sans",Arial,sans-serif;color:var(--text);position:relative}
.piece{position:absolute;overflow:hidden;box-shadow:0 6px 14px rgba(0,0,0,.22)}
.dark{background:var(--ink);color:#fff}
.light{background:var(--paper)}
.wave{position:absolute;left:0;bottom:0;width:100%;display:block}
.brand{position:absolute;line-height:1}
.brand-name{font-family:"Poppins",Arial,sans-serif;font-weight:800;letter-spacing:-.5px;display:block}
.brand-tag{font-family:"Poppins",Arial,sans-serif;font-weight:500;display:block;white-space:nowrap}
.dark .brand-name,.dark .brand-tag{color:#fff}
.light .brand-name,.light .brand-tag{color:var(--ink)}
.contact{position:absolute;list-style:none;line-height:1.45}
.contact li{display:flex;align-items:center;gap:3px;white-space:nowrap}
.contact svg{flex:none}
.divider{position:absolute;width:1px;background:var(--red)}
.person{font-family:"Poppins",Arial,sans-serif;position:absolute;line-height:1.1}
.person .first{color:var(--red);font-weight:500}
.person .last{color:#fff;font-weight:400}
.person .role{display:block;font-weight:500;color:#fff}
.pattern{position:absolute;background:linear-gradient(160deg,#55545c 0%,#2d2c35 35%,#1a1922 100%)}

/* envelope */
.envelope-front{left:51px;top:55px;width:282px;height:125px}
.envelope-back{left:52px;top:194px;width:281px;height:125px}
.envelope-flap{position:absolute;left:4px;top:0;right:4px;height:42px;background:var(--ink-soft);border-radius:0 0 10px 10px;box-shadow:0 3px 6px rgba(0,0,0,.35)}
.flap-seal{position:absolute;left:134px;top:14px;width:14px;height:14px;border-radius:50%;background:var(--red)}

/* cards */
.card{border-radius:14px}
.card-back{left:53px;top:329px;width:274px;height:157px}
.card-front{left:53px;top:502px;width:274px;height:156px}

/* letterhead */
.letterhead{left:367px;top:57px;width:330px;height:466px;font-size:6.4px}
.letter-meta{position:absolute;left:18px;top:117px;line-height:1.3}
.letter-meta .recipient{font-weight:700;font-size:8px;margin-top:7px}
.letter-meta .addr{margin-top:6px}
.salutation{position:absolute;left:18px;top:183px;font-weight:700;font-size:8px}
.letter-body{position:absolute;left:18px;top:200px;width:294px;text-align:justify;line-height:1.36;color:var(--muted)}
.letter-body p{margin-bottom:8.6px}
.signature-mark{position:absolute;left:18px;top:349px;width:88px;height:21px;background:linear-gradient(90deg,#d6d6d6,#eeeeee)}
.signer{position:absolute;left:18px;top:372px;line-height:1.1}
.signer strong{font-family:"Poppins",Arial,sans-serif;font-size:14px;font-weight:700;display:block}

/* email signature */
.email-signature{left:366px;top:546px;width:330px;height:110px}
.social{position:absolute;left:208px;bottom:4px;display:flex;gap:4px}
.social span{width:7px;height:7px;border-radius:50%;background:#fff}

/* folder */
.folder-cover{left:728px;top:48px;width:122px;height:234px}
.cover-art{position:absolute;left:8px;top:30px;width:106px;height:120px;background:radial-gradient(circle at 55% 40%,#e04a4a 0%,#b3141e 55%,var(--ink) 78%)}
.folder-inside{left:912px;top:62px;width:228px;height:208px;background:linear-gradient(90deg,#f4f4f4,#dcdcdc 50%,#f1f1f1 50%,#cfcfcf)}
.pocket{position:absolute;bottom:0;width:114px;height:70px;background:var(--red)}
.pocket-left{left:0;clip-path:polygon(0 0,60% 0,100% 40%,100% 100%,0 100%)}
.pocket-right{right:0;clip-path:polygon(0 40%,40% 0,100% 0,100% 100%,0 100%)}
.pocket .mark{position:absolute;top:34px;width:10px;height:10px;border-radius:50%;background:#fff}

/* notebook */
.notebook-cover{left:818px;top:292px;width:250px;height:150px;border-radius:3px}
.spiral{position:absolute;left:0;top:0;bottom:0;width:8px;background:repeating-linear-gradient(180deg,#bcbcbc 0 2px,#4b4b4b 2px 4px)}
.notepad{left:782px;top:462px;width:274px;height:192px}
.notepad-page{position:absolute;top:0;width:132px;height:192px;background:var(--paper)}
.notepad-page.left{left:0}
.notepad-page.right{right:0}
.binding{position:absolute;left:132px;top:0;width:10px;height:192px;background:repeating-linear-gradient(180deg,#9a9a9a 0 2px,#f0f0f0 2px 4px)}
.notes-label{position:absolute;left:10px;top:14px;font-family:"Poppins",Arial,sans-serif;font-size:4.5px;color:var(--red);line-height:1.3}
.notes-label em{display:block;color:#777;font-style:italic}
.rules{position:absolute;left:10px;right:8px;top:36px;height:120px;background:repeating-linear-gradient(180deg,transparent 0 8.6px,var(--line) 8.6px 9.4px)}
.page-tint{position:absolute;left:26px;top:58px;width:82px;height:96px;background:radial-gradient(circle,var(--tint) 0%,rgba(247,230,224,0) 70%)}
</style>
</head>
<body>

<!-- Envelope front -->
<section class="piece dark envelope-front" aria-label="Envelope front">
  <div class="brand" style="right:12px;top:10px;text-align:right">
    <span class="brand-name" style="font-size:22px">Brenvik</span>
    <span class="brand-tag" style="font-size:4.4px">Tape and Packaging Specialists</span>
  </div>
  <ul class="contact" style="left:208px;top:60px;font-size:5px;line-height:1.3">
    <li>1180 Harbourline Rd. Suite 300</li>
    <li>Hamilton, ON L8P 4R5</li>
  </ul>
  <ul class="contact" style="left:208px;top:80px;font-size:5px;line-height:1.35">
    <li><svg width="5" height="5" viewBox="0 0 10 10"><circle cx="5" cy="5" r="5" fill="#e31b2c"/></svg>(555) 214-3087</li>
    <li><svg width="5" height="5" viewBox="0 0 10 10"><circle cx="5" cy="5" r="5" fill="#e31b2c"/></svg>hello@brenvik.ca</li>
    <li><svg width="5" height="5" viewBox="0 0 10 10"><circle cx="5" cy="5" r="5" fill="#e31b2c"/></svg>www.brenvik.ca</li>
  </ul>
  <svg class="wave" height="30" viewBox="0 0 300 60" preserveAspectRatio="none">
    <path d="M0 8 C60 40 150 42 205 26 C245 15 280 26 300 60 L0 60Z" fill="#e31b2c"/>
    <path d="M0 2 C60 34 150 36 205 20 C245 9 280 20 300 54" fill="none" stroke="#fff" stroke-width="3"/>
  </svg>
</section>

<!-- Envelope back -->
<section class="piece dark envelope-back" aria-label="Envelope back">
  <div class="envelope-flap"><span class="flap-seal"></span></div>
</section>

<!-- Business card back -->
<section class="piece dark card card-back" aria-label="Business card back">
  <div class="pattern" role="img" aria-label="Repeating leaf pattern in dark grey tones" style="inset:0"></div>
  <div class="brand" style="left:168px;top:106px">
    <span class="brand-name" style="font-size:21px">Brenvik</span>
    <span class="brand-tag" style="font-size:4.2px">Tape and Packaging Specialists</span>
  </div>
</section>

<!-- Business card front -->
<section class="piece dark card card-front" aria-label="Business card front">
  <div class="brand" style="left:9px;top:63px">
    <span class="brand-name" style="font-size:26px">Brenvik</span>
    <span class="brand-tag" style="font-size:5.2px">Tape and Packaging Specialists</span>
  </div>
  <span class="divider" style="left:137px;top:22px;height:90px"></span>
  <div class="person" style="left:161px;top:34px;font-size:15px">
    <span class="first">Marta</span> <span class="last">Kovel</span>
    <span class="role" style="font-size:7.4px;margin-top:2px">Founder &amp; CEO</span>
  </div>
  <ul class="contact" style="left:161px;top:77px;font-size:7.6px;line-height:1.3">
    <li><svg width="6" height="6" viewBox="0 0 10 10"><path d="M2 1l2 2-1 1.5c.6 1.3 1.2 1.9 2.5 2.5L7 6l2 2-1.5 1.5C4 9 1 6 .5 2.5Z" fill="#e31b2c"/></svg>(555) 214-3087</li>
    <li><svg width="6" height="6" viewBox="0 0 10 10"><circle cx="5" cy="5" r="4.5" fill="#e31b2c"/></svg>hello@brenvik.com</li>
    <li><svg width="6" height="6" viewBox="0 0 10 10"><rect x=".5" y="2" width="9" height="6.5" rx="1" fill="#e31b2c"/></svg>www.brenvik.com</li>
  </ul>
  <svg class="wave" height="42" viewBox="0 0 300 60" preserveAspectRatio="none">
    <path d="M0 8 C60 40 150 40 205 24 C245 13 280 24 300 60 L0 60Z" fill="#e31b2c"/>
    <path d="M0 2 C60 34 150 34 205 18 C245 7 280 18 300 54" fill="none" stroke="#fff" stroke-width="2.5"/>
  </svg>
  <p style="position:absolute;left:0;right:0;bottom:8px;text-align:center;font-family:Poppins,Arial,sans-serif;font-size:7.4px;color:#fff">1180 Harbourline Rd. Suite 300 Hamilton, ON L8P 4R5</p>
</section>

<!-- Letterhead -->
<section class="piece light letterhead" aria-label="Letterhead">
  <div class="brand" style="left:18px;top:17px">
    <span class="brand-name" style="font-size:24px">Brenvik</span>
    <span class="brand-tag" style="font-size:4.8px">Tape and Packaging Specialists</span>
  </div>
  <ul class="contact" style="right:18px;top:16px;font-family:Poppins,Arial,sans-serif;font-size:6.9px;line-height:1.32;text-align:right">
    <li style="justify-content:flex-end">(555) 214-3087 <svg width="6" height="6" viewBox="0 0 10 10"><circle cx="5" cy="5" r="4.5" fill="#e31b2c"/></svg></li>
    <li style="justify-content:flex-end">hello@brenvik.com <svg width="6" height="6" viewBox="0 0 10 10"><circle cx="5" cy="5" r="4.5" fill="#e31b2c"/></svg></li>
    <li style="justify-content:flex-end">www.brenvik.com <svg width="6" height="6" viewBox="0 0 10 10"><circle cx="5" cy="5" r="4.5" fill="#e31b2c"/></svg></li>
    <li style="justify-content:flex-end">1180 Harbourline Rd. Suite 300 <svg width="6" height="6" viewBox="0 0 10 10"><path d="M5 0a3.5 3.5 0 0 1 3.5 3.5C8.5 6 5 10 5 10S1.5 6 1.5 3.5A3.5 3.5 0 0 1 5 0Z" fill="#e31b2c"/></svg></li>
    <li style="justify-content:flex-end;padding-right:9px">Hamilton, ON L8P 4R5</li>
  </ul>
  <div class="letter-meta">
    <p>August-05-2019</p>
    <p class="recipient">Petra Lindqvist</p>
    <p>Director</p>
    <p class="addr">1180 Harbourline Rd. Suite 300<br>Hamilton, ON L8P 4R5</p>
  </div>
  <p class="salutation">Petra Lindqvist</p>
  <div class="letter-body">
    <p>Lorem ipsum dolor sit amet, consectetuer adipiscing elit, sed diam nonummy nibh euismod tincidunt ut laoreet dolore magna aliquam erat volutpat. Ut wisi enim ad minim veniam, quis nostrud exerci tation ullamcorper suscipit lobortis</p>
    <p>Lorem ipsum dolor sit amet, cons ectetuer adipiscing elit, sed diam nonummy nibh euismod tincidunt ut laoreet dolore magna aliquam erat volutpat. Ut wisi enim ad minim veniam, quis nostrud exerci tation ullamcorper suscipit lobortis nisl ut aliquip ex ea commodo consequat. Lorem ipsum dolor sit amet, consectetuer olutpat. Ut wisi enim ad minim veniam, quis nostrud exerci tation ullamcorper suscipit lobortis nisl ut aliquip ex ea commodo consequat. Duis autem</p>
    <p>vel eum iriure dolor in hendrerit in vulputate velit esse molestie consequat, vel illum dolore eu feugiat nulla facilisis at vero eros et accumsan et iusto odio dignissim qui blandit praesent luptatum zzril delenit augue duis dolore te feugait nulla facilisi. Lorem ipsum dolor sit amet, cons ectetuer adipiscing elit, sed diam nonummy nibh euismod tincidunt ut laoreet dolore magna aliquam erat volutpat. Ut wisi enim .</p>
  </div>
  <div class="signature-mark" role="img" aria-label="Handwritten signature"></div>
  <div class="signer"><strong>Jonah Merrit</strong>Co-Founder</div>
  <svg class="wave" height="40" viewBox="0 0 300 60" preserveAspectRatio="none">
    <path d="M0 12 C60 44 150 44 205 26 C245 14 280 26 300 60 L0 60Z" fill="#e31b2c"/>
    <path d="M0 2 C60 34 150 34 205 16 C245 4 280 16 300 54" fill="none" stroke="#1c1b27" stroke-width="4"/>
    <path d="M0 7 C60 39 150 39 205 21 C245 9 280 21 300 58" fill="none" stroke="#fff" stroke-width="2.5"/>
  </svg>
</section>

<!-- Email signature -->
<section class="piece dark email-signature" aria-label="Email signature">
  <div class="brand" style="left:16px;top:34px">
    <span class="brand-name" style="font-size:30px">Brenvik</span>
    <span class="brand-tag" style="font-size:6px">Tape and Packaging Specialists</span>
  </div>
  <span class="divider" style="left:165px;top:16px;height:74px"></span>
  <div class="person" style="left:194px;top:13px;font-size:15px">
    <span class="first">Marta</span> <span class="last">Kovel</span>
    <span class="role" style="font-size:7px;margin-top:1px">Founder &amp; CEO</span>
  </div>
  <ul class="contact" style="left:194px;top:43px;font-size:6.8px;line-height:1.22">
    <li>72 Cedar Row</li>
    <li>Kingsford, Kent, KF2 8QL</li>
  </ul>
  <ul class="contact" style="left:194px;top:62px;font-size:6.8px;line-height:1.22">
    <li><svg width="5" height="5" viewBox="0 0 10 10"><circle cx="5" cy="5" r="4.5" fill="#e31b2c"/></svg>(555) 214-3087</li>
    <li><svg width="5" height="5" viewBox="0 0 10 10"><circle cx="5" cy="5" r="4.5" fill="#e31b2c"/></svg>www.brenvik-supply.com</li>
    <li><svg width="5" height="5" viewBox="0 0 10 10"><circle cx="5" cy="5" r="4.5" fill="#e31b2c"/></svg>office@brenvik-supply.com</li>
  </ul>
  <svg class="wave" height="28" viewBox="0 0 300 60" preserveAspectRatio="none">
    <path d="M0 6 C60 40 150 40 205 22 C245 10 280 22 300 60 L0 60Z" fill="#e31b2c"/>
    <path d="M0 0 C60 34 150 34 205 16 C245 4 280 16 300 54" fill="none" stroke="#fff" stroke-width="3"/>
  </svg>
  <div class="social" aria-label="Social links"><span></span><span></span><span></span><span></span><span></span></div>
</section>

<!-- Presentation folder cover -->
<section class="piece dark folder-cover" aria-label="Presentation folder cover">
  <div class="cover-art" role="img" aria-label="Large red leaf artwork on dark background"></div>
  <div class="brand" style="right:8px;top:192px;text-align:right">
    <span class="brand-name" style="font-size:15px">Brenvik</span>
    <span class="brand-tag" style="font-size:3px">Tape and Packaging Specialists</span>
  </div>
  <svg class="wave" height="22" viewBox="0 0 300 60" preserveAspectRatio="none">
    <path d="M0 6 C60 40 150 40 205 22 C245 10 280 22 300 60 L0 60Z" fill="#e31b2c"/>
    <path d="M0 0 C60 34 150 34 205 16 C245 4 280 16 300 54" fill="none" stroke="#fff" stroke-width="3"/>
  </svg>
</section>

<!-- Presentation folder inside -->
<section class="piece folder-inside" aria-label="Presentation folder inside">
  <div class="pocket pocket-left"><span class="mark" style="left:44px"></span></div>
  <div class="pocket pocket-right"><span class="mark" style="left:60px"></span></div>
</section>

<!-- Notebook cover -->
<section class="piece dark notebook-cover" aria-label="Notebook cover">
  <div class="pattern" role="img" aria-label="Repeating leaf pattern in dark grey tones" style="inset:0"></div>
  <div class="spiral"></div>
  <div class="brand" style="right:14px;top:98px;text-align:right">
    <span class="brand-name" style="font-size:14px">Brenvik</span>
    <span class="brand-tag" style="font-size:3px">Tape and Packaging Specialists</span>
  </div>
  <svg class="wave" height="26" viewBox="0 0 300 60" preserveAspectRatio="none">
    <path d="M0 6 C60 40 150 40 205 22 C245 10 280 22 300 60 L0 60Z" fill="#e31b2c"/>
    <path d="M0 0 C60 34 150 34 205 16 C245 4 280 16 300 54" fill="none" stroke="#fff" stroke-width="3"/>
  </svg>
</section>

<!-- Notepad spread -->
<section class="piece notepad" aria-label="Notepad pages">
  <div class="notepad-page left">
    <p class="notes-label">Notes<em>Date Of ____________</em></p>
    <div class="brand" style="right:8px;top:10px;text-align:right;border-bottom:1px solid #e31b2c;padding-bottom:1px">
      <span class="brand-name" style="font-size:10px;color:#1c1b27">Brenvik</span>
      <span class="brand-tag" style="font-size:2.4px;color:#1c1b27">Tape and Packaging Specialists</span>
    </div>
    <div class="page-tint"></div>
    <div class="rules"></div>
    <svg class="wave" height="14" viewBox="0 0 300 60" preserveAspectRatio="none">
      <path d="M0 12 C60 44 150 44 205 26 C245 14 280 26 300 60 L0 60Z" fill="#e31b2c"/>
      <path d="M0 4 C60 36 150 36 205 18 C245 6 280 18 300 56" fill="none" stroke="#1c1b27" stroke-width="4"/>
    </svg>
  </div>
  <div class="binding"></div>
  <div class="notepad-page right">
    <p class="notes-label">Notes<em>Date Of ____________</em></p>
    <div class="brand" style="right:8px;top:10px;text-align:right;border-bottom:1px solid #e31b2c;padding-bottom:1px">
      <span class="brand-name" style="font-size:10px;color:#1c1b27">Brenvik</span>
      <span class="brand-tag" style="font-size:2.4px;color:#1c1b27">Tape and Packaging Specialists</span>
    </div>
    <div class="page-tint"></div>
    <div class="rules"></div>
    <svg class="wave" height="14" viewBox="0 0 300 60" preserveAspectRatio="none">
      <path d="M0 12 C60 44 150 44 205 26 C245 14 280 26 300 60 L0 60Z" fill="#e31b2c"/>
      <path d="M0 4 C60 36 150 36 205 18 C245 6 280 18 300 56" fill="none" stroke="#1c1b27" stroke-width="4"/>
    </svg>
  </div>
</section>

</body>
</html>
```